Business Card for Ferncliff Massage

I need a business card for my massage therapy & cannabis oil practice. I already have a logo,the "massage" got edited out of this file. I will send the original soon. I need these elements to be on the card:
web: FerncliffMassage.example
ph: 417/283-9061
email: Mirela.Dawkant@mailbox.example
Other slogans, statements to consider:
Science Geek, Massage Therapist, Neuromuscular Therapy, Cannabis Spa Treatments, Raindrop Therapy, Essential Oils
Target Market(s)
women between 20 & 65, people with enough $ to afford regular massage, people who recently had a motor vehicle accident, Halvora HMP insured
Industry/Entity Type
Massage Therapy
Contact Information for Business Card
I would like to see my bear logo featured; contact details, greens & blues preferred colors.

```html
<!DOCTYPE html>
<html lang="en">
<head>
<meta charset="utf-8">
<title>Ferncliff Massage – Business Card</title>
<link rel="stylesheet" href="https://fonts.googleapis.com/css2?family=Encode+Sans+Condensed:wght@400&family=Open+Sans:wght@400;700&display=swap">
<style>
  :root {
    --backdrop: #2b2b2b;
    --card-white: #ffffff;
    --fern-green: #3b8a40;
    --earth-brown: #766657;
    --earth-brown-light: #a0958a;
    --text-grey: #555555;
    --text-white: #ffffff;
  }
  * { margin: 0; padding: 0; box-sizing: border-box; }
  html, body {
    width: 1200px; height: 987px; overflow: hidden;
    background: var(--backdrop);
    font-family: "Open Sans", Arial, sans-serif;
  }
  .canvas { position: relative; width: 1200px; height: 987px; }

  .card {
    position: absolute; left: 293px; width: 615px; height: 350px;
    border-radius: 16px; overflow: hidden;
  }
  .card-front { top: 130px; background: var(--card-white); }
  .card-back { top: 505px; background: var(--earth-brown); }

  /* Front */
  .brand-name {
    position: absolute; right: 35px; top: 154px;
    font-family: "Encode Sans Condensed", "Arial Narrow", sans-serif;
    font-weight: 400; font-size: 44px; line-height: 1;
    color: var(--earth-brown);
  }
  .person-name {
    position: absolute; left: 33px; top: 174px;
    font-weight: 700; font-size: 21px; line-height: 26px;
    color: var(--fern-green); letter-spacing: 0.3px;
  }
  .person-title {
    position: absolute; left: 33px; top: 208px;
    font-size: 16px; line-height: 22px; color: var(--text-grey);
  }
  .divider {
    position: absolute; left: 33px; top: 240px; width: 547px; height: 1.5px;
    background: var(--earth-brown-light);
  }
  .contact-list {
    position: absolute; left: 33px; top: 250px; list-style: none;
  }
  .contact-list li {
    display: flex; align-items: center; gap: 8px;
    font-size: 16px; line-height: 23.5px; color: var(--text-grey);
  }
  .contact-list svg { width: 15px; height: 15px; flex: none; fill: var(--fern-green); }
  .edge-band { position: absolute; left: 0; bottom: 0; width: 615px; height: 8px; }

  /* Back */
  .back-brand {
    position: absolute; left: 41px; top: 36px;
    font-family: "Encode Sans Condensed", "Arial Narrow", sans-serif;
    font-weight: 400; font-size: 68px; line-height: 1; color: var(--text-white);
  }
  .back-web {
    position: absolute; left: 42px; top: 106px;
    font-size: 16px; line-height: 22px; letter-spacing: 0.8px; color: var(--text-white);
  }
  .services-heading {
    position: absolute; left: 42px; top: 140px;
    font-weight: 700; font-size: 20px; line-height: 26px; color: var(--text-white);
  }
  .services-list {
    position: absolute; left: 42px; top: 169px; list-style: none;
  }
  .services-list li {
    font-size: 16px; line-height: 24.6px; color: var(--text-white);
  }
  .services-list li::before { content: "•"; margin-right: 9px; }
</style>
</head>
<body>
<main class="canvas">
  <section class="card card-front" aria-label="Card front">
    <div class="brand-name">Ferncliff</div>
    <h1 class="person-name">TOBIN ARLOW</h1>
    <p class="person-title">CEO/Founder</p>
    <div class="divider"></div>
    <ul class="contact-list">
      <li><svg viewBox="0 0 24 24" aria-hidden="true"><path d="M6.6 10.8a15.2 15.2 0 0 0 6.6 6.6l2.2-2.2a1 1 0 0 1 1-.25 11.4 11.4 0 0 0 3.6.57 1 1 0 0 1 1 1V20a1 1 0 0 1-1 1A17 17 0 0 1 3 4a1 1 0 0 1 1-1h3.5a1 1 0 0 1 1 1c0 1.25.2 2.45.57 3.57a1 1 0 0 1-.25 1z"/></svg>417/283-9061</li>
      <li><svg viewBox="0 0 24 24" aria-hidden="true"><path d="M2 5h20v14H2z M3.5 6.5 12 12.5l8.5-6" stroke="#fff" stroke-width="1.6"/></svg>Mirela.Dawkant@mailbox.example</li>
      <li><svg viewBox="0 0 24 24" aria-hidden="true"><circle cx="12" cy="12" r="10"/><path d="M7 7c2 1 3 3 2 5s1 3 2 5M14 4c-1 2 1 3 3 3s2 3 1 5" stroke="#fff" stroke-width="1.6" fill="none"/></svg>FerncliffMassage.example</li>
    </ul>
    <svg class="edge-band" viewBox="0 0 615 8" preserveAspectRatio="none" aria-hidden="true">
      <rect x="0" y="0" width="615" height="8" fill="var(--earth-brown)"/>
      <polygon points="0,0 404,0 399,8 0,8" fill="var(--fern-green)"/>
    </svg>
  </section>

  <section class="card card-back" aria-label="Card back">
    <div class="back-brand">Ferncliff</div>
    <p class="back-web">www.FerncliffMassage.example</p>
    <h2 class="services-heading">SERVICES</h2>
    <ul class="services-list">
      <li>Science Geek</li>
      <li>Massage Therapist</li>
      <li>Neuromuscular Therapy</li>
      <li>Cannabis Spa Treatments</li>
      <li>Raindrop Therapy</li>
      <li>Essential Oils</li>
    </ul>
  </section>
</main>
</body>
</html>
```